Business Cards

I'd like help creating business cards with the full logo "Veltrona Capital Partners" on the back of the card (navy background with white writing), and abbreviated logo "VCP" on the front. Would like to list name, title, phone number, email, and website listed on front of card. Would like to keep very simple. Front font Arial or similar.

```html
<!DOCTYPE html>
<html lang="en">
<head>
<meta charset="utf-8">
<title>Veltrona Capital Partners – Business Cards</title>
<link rel="stylesheet" href="https://fonts.googleapis.com/css2?family=Arimo:wght@400;700&display=swap">
<style>
  :root {
    --backdrop: #333e45;
    --navy: #021b8f;
    --white: #ffffff;
    --ink: #111111;
    --card-shadow: 0 14px 24px rgba(0, 0, 0, 0.45);
  }
  html, body {
    margin: 0;
    padding: 0;
    width: 1200px;
    height: 1200px;
    overflow: hidden;
    background: var(--backdrop);
    font-family: "Arimo", Arial, sans-serif;
  }
  .canvas {
    position: relative;
    width: 1200px;
    height: 1200px;
  }
  .card {
    position: absolute;
    left: 250px;
    width: 700px;
    height: 404px;
    box-shadow: var(--card-shadow);
    overflow: hidden;
  }
  /* Back of card */
  .card-back {
    top: 140px;
    background: var(--navy);
    color: var(--white);
  }
  .brand-lockup {
    position: absolute;
    left: 0;
    right: 0;
    top: 150px;
    text-align: center;
    font-weight: 700;
  }
  .brand-name {
    display: block;
    font-size: 62px;
    letter-spacing: 4px;
    line-height: 1;
  }
  .brand-tagline {
    display: block;
    margin-top: 22px;
    font-size: 24px;
    letter-spacing: 15px;
    line-height: 1;
    padding-left: 15px;
  }
  /* Front of card */
  .card-front {
    top: 651px;
    background: var(--white);
  }
  .name-accent {
    position: absolute;
    left: 0;
    top: 69px;
    width: 25px;
    height: 51px;
    background: var(--navy);
  }
  .holder-name {
    position: absolute;
    left: 50px;
    top: 65px;
    margin: 0;
    font-size: 28px;
    font-weight: 700;
    color: var(--navy);
    letter-spacing: -0.3px;
    line-height: 1;
  }
  .holder-title {
    position: absolute;
    left: 50px;
    top: 100px;
    margin: 0;
    font-size: 21px;
    font-weight: 400;
    color: var(--ink);
    line-height: 1;
  }
  .short-mark {
    position: absolute;
    left: 468px;
    top: 68px;
    width: 170px;
    text-align: center;
    font-size: 68px;
    font-weight: 700;
    color: var(--navy);
    letter-spacing: 1px;
    line-height: 1;
  }
  .contact-band {
    position: absolute;
    left: 0;
    right: 0;
    top: 232px;
    bottom: 0;
    background: var(--navy);
  }
  .contact-list {
    list-style: none;
    margin: 0;
    padding: 0;
    position: absolute;
    left: 52px;
    top: 47px;
    color: var(--white);
    font-size: 18px;
  }
  .contact-list li {
    display: flex;
    align-items: center;
    height: 28px;
  }
  .contact-icon {
    width: 15px;
    height: 15px;
    margin-right: 15px;
    fill: var(--white);
  }
</style>
</head>
<body>
<main class="canvas">
  <section class="card card-back" aria-label="Back of business card">
    <div class="brand-lockup">
      <span class="brand-name">VELTRONA</span>
      <span class="brand-tagline">CAPITAL PARTNERS</span>
    </div>
  </section>

  <section class="card card-front" aria-label="Front of business card">
    <div class="name-accent"></div>
    <h1 class="holder-name">MILES HARROW</h1>
    <p class="holder-title">(Co-Founder)</p>
    <div class="short-mark">VCP</div>

    <div class="contact-band">
      <ul class="contact-list">
        <li>
          <svg class="contact-icon" viewBox="0 0 16 16" aria-hidden="true">
            <path d="M1 5c0-2 3-3 7-3s7 1 7 3v1.5h-3.5V5h-7v1.5H1z"/>
            <path d="M3 8l2-2h6l2 2v6H3z"/>
            <circle cx="8" cy="10.5" r="1.6" fill="#021b8f"/>
          </svg>
          <span>5550148823</span>
        </li>
        <li>
          <svg class="contact-icon" viewBox="0 0 16 16" aria-hidden="true">
            <path d="M1 4h14v1.2L8 9 1 5.2z"/>
            <path d="M1 6.6 8 10.4l7-3.8V12H1z"/>
          </svg>
          <span>veltronacp@mailbox.com</span>
        </li>
        <li>
          <svg class="contact-icon" viewBox="0 0 16 16" aria-hidden="true">
            <circle cx="8" cy="8" r="7"/>
            <path d="M5 4.5c1.5 0 2 1 1.5 2s-2 1-1.5 2.5 1.5 1 1.5 2.5M10 3.5c-.5 1.5.5 2 1.5 2.5s.5 2-1 2.5" stroke="#021b8f" stroke-width="1.3" fill="none"/>
          </svg>
          <span>www.veltronacp.com</span>
        </li>
      </ul>
    </div>
  </section>
</main>
</body>
</html>
```